Mosvane Design

Looking for Mosvane banner and square design:
Mosvane Banner
W:1600 px H:400 px
Square
120x120

Logo attached.

Description: Data-Driven stock market portfolio management using quantitative analysis.

```html
<!DOCTYPE html>
<html lang="en">
<head>
<meta charset="utf-8">
<title>Mosvane – Banner and Square</title>
<link href="https://fonts.googleapis.com/css2?family=Barlow+Condensed:wght@500;700&family=Montserrat:wght@600&display=swap" rel="stylesheet">
<style>
  :root {
    --canvas: #ececec;
    --brand-blue: #1460a8;
    --brand-blue-deep: #1a4f9c;
    --headline-blue: #0f5d9e;
    --panel-light: #eaf0f7;
    --stripe-light: #c9d6e6;
    --white: #ffffff;
  }
  * { margin: 0; padding: 0; box-sizing: border-box; }
  html, body { width: 1200px; height: 900px; overflow: hidden; background: var(--canvas); }
  .canvas { position: relative; width: 1200px; height: 900px; }

  /* Banner */
  .banner {
    position: absolute; left: 63px; top: 97px; width: 1074px; height: 268px; overflow: hidden;
    background: linear-gradient(90deg, var(--white) 0%, var(--panel-light) 60%);
  }
  .banner-stripes { position: absolute; left: 0; top: 0; width: 180px; height: 268px; }
  .banner-stripe {
    position: absolute; left: 0; width: 180px; height: 3px;
    background: linear-gradient(90deg, var(--stripe-light) 0%, rgba(201,214,230,0) 100%);
  }
  .banner-blue { position: absolute; left: 0; top: 0; width: 1074px; height: 268px; }
  .banner-stripes-right { position: absolute; right: 0; top: 0; width: 190px; height: 268px; }
  .banner-stripes-right .banner-stripe {
    left: auto; right: 0; width: 190px; height: 2px;
    background: linear-gradient(90deg, rgba(255,255,255,0) 0%, rgba(255,255,255,0.3) 100%);
  }
  .banner-brand {
    position: absolute; left: 208px; top: 40px; display: flex; align-items: center; gap: 8px;
  }
  .brand-dot { width: 36px; height: 36px; border-radius: 50%; background: var(--brand-blue); }
  .brand-name {
    font-family: "Montserrat", sans-serif; font-weight: 600; font-size: 19px;
    letter-spacing: 0.5px; color: var(--brand-blue);
  }
  .banner-headline {
    position: absolute; left: 205px; top: 85px;
    font-family: "Barlow Condensed", sans-serif; color: var(--headline-blue);
    font-size: 37px; line-height: 39.5px; text-transform: uppercase;
  }
  .headline-lead { font-weight: 500; display: block; }
  .headline-strong { font-weight: 700; display: block; }
  .banner-illustration {
    position: absolute; left: 615px; top: 28px; width: 255px; height: 200px; border-radius: 24px;
    background: radial-gradient(ellipse at 50% 50%, rgba(255,255,255,0.85) 0%, rgba(220,232,246,0.55) 45%, rgba(20,96,168,0) 75%);
  }

  /* Square */
  .square {
    position: absolute; left: 416px; top: 435px; width: 368px; height: 368px; overflow: hidden;
    background: linear-gradient(180deg, var(--brand-blue-deep) 0%, var(--brand-blue) 100%);
  }
  .square-stripe { position: absolute; width: 3px; height: 100px; }
  .square-stripe.top { top: 0; background: linear-gradient(180deg, rgba(255,255,255,0.35) 0%, rgba(255,255,255,0) 100%); }
  .square-stripe.bottom { bottom: 0; background: linear-gradient(0deg, rgba(255,255,255,0.35) 0%, rgba(255,255,255,0) 100%); }
  .square-mark {
    position: absolute; left: 134px; top: 99px; width: 100px; height: 100px; border-radius: 50%;
    background: var(--white);
  }
  .square-name {
    position: absolute; left: 0; top: 206px; width: 368px; text-align: center;
    font-family: "Montserrat", sans-serif; font-weight: 600; font-size: 36px;
    letter-spacing: 1px; color: var(--white);
  }
</style>
</head>
<body>
<main class="canvas">

  <section class="banner" aria-label="Mosvane banner">
    <div class="banner-stripes">
      <span class="banner-stripe" style="top:35px"></span>
      <span class="banner-stripe" style="top:57px"></span>
      <span class="banner-stripe" style="top:80px"></span>
      <span class="banner-stripe" style="top:102px"></span>
      <span class="banner-stripe" style="top:124px"></span>
      <span class="banner-stripe" style="top:146px"></span>
      <span class="banner-stripe" style="top:168px"></span>
      <span class="banner-stripe" style="top:191px"></span>
      <span class="banner-stripe" style="top:213px"></span>
      <span class="banner-stripe" style="top:235px"></span>
    </div>

    <svg class="banner-blue" viewBox="0 0 1074 268" aria-hidden="true">
      <defs>
        <linearGradient id="blueField" x1="0" x2="1" y1="0" y2="0">
          <stop offset="0" stop-color="#1460a8"/>
          <stop offset="1" stop-color="#1a4f9c"/>
        </linearGradient>
      </defs>
      <path d="M648 0 C 700 30, 625 200, 670 268 L 1074 268 L 1074 0 Z" fill="#dfe3e8"/>
      <path d="M655 0 C 705 30, 632 200, 677 268 L 1074 268 L 1074 0 Z" fill="url(#blueField)"/>
    </svg>

    <div class="banner-stripes-right">
      <span class="banner-stripe" style="top:35px"></span>
      <span class="banner-stripe" style="top:57px"></span>
      <span class="banner-stripe" style="top:80px"></span>
      <span class="banner-stripe" style="top:102px"></span>
      <span class="banner-stripe" style="top:124px"></span>
      <span class="banner-stripe" style="top:146px"></span>
      <span class="banner-stripe" style="top:168px"></span>
      <span class="banner-stripe" style="top:191px"></span>
      <span class="banner-stripe" style="top:213px"></span>
      <span class="banner-stripe" style="top:235px"></span>
    </div>

    <div class="banner-illustration" role="img" aria-label="Isometric illustration of analysts working on floating platforms with data dashboards, charts and a server, linked by lines"></div>

    <div class="banner-brand">
      <span class="brand-dot"></span>
      <span class="brand-name">MOSVANE</span>
    </div>

    <h1 class="banner-headline">
      <span class="headline-lead">Data-Driven Stock Market</span>
      <span class="headline-strong">Portfolio Management</span>
      <span class="headline-strong">Using Quantitative Analysis.</span>
    </h1>
  </section>

  <section class="square" aria-label="Mosvane square">
    <span class="square-stripe top" style="left:73px"></span>
    <span class="square-stripe top" style="left:98px"></span>
    <span class="square-stripe top" style="left:122px"></span>
    <span class="square-stripe top" style="left:147px"></span>
    <span class="square-stripe top" style="left:171px"></span>
    <span class="square-stripe top" style="left:196px"></span>
    <span class="square-stripe top" style="left:220px"></span>
    <span class="square-stripe top" style="left:245px"></span>
    <span class="square-stripe top" style="left:269px"></span>
    <span class="square-stripe top" style="left:294px"></span>
    <span class="square-stripe bottom" style="left:73px"></span>
    <span class="square-stripe bottom" style="left:98px"></span>
    <span class="square-stripe bottom" style="left:122px"></span>
    <span class="square-stripe bottom" style="left:147px"></span>
    <span class="square-stripe bottom" style="left:171px"></span>
    <span class="square-stripe bottom" style="left:196px"></span>
    <span class="square-stripe bottom" style="left:220px"></span>
    <span class="square-stripe bottom" style="left:245px"></span>
    <span class="square-stripe bottom" style="left:269px"></span>
    <span class="square-stripe bottom" style="left:294px"></span>

    <span class="square-mark"></span>
    <p class="square-name">MOSVANE</p>
  </section>

</main>
</body>
</html>
```